Willow Cradle Pregnancy and Baby Massage

I need a web design for a new business, WILLOW CRADLE PREGNANCY AND BABY MASSAGE that I am in the process of setting up in the suburbs of Perth, Western Australia. The business is owned and operated by myself and my intention is to service Pregnant Mothers and Parents of Young Babies that would benefit from massage. I would like to have a "Home Page" and pages for "About Me", "Pregnancy Massage", "Baby Massage", a Pricing Page for Pregnancy Massage Sessions, a Pricing Page for Baby Massage Sessions, and a "Contact Me" page to allow clients to either contact me with queries or book available pregnancy massage sessions on a particular day of the week. I would also like a "News" page that would include articles I have written, news about new courses and a link to my Facebook page (yet to be set up). I would like to keep the colour schemes similar to my logo design colours. I need the design to be easy to follow and to appeal to a younger audience (20's to mid 30's).
The target audience is pregnant mothers-to-be wishing to receive massage treatments, and new parents and grandparents of small babies that would like to learn how to massage their babies.
The look and feel should be modern, professional, elegant and feminine.
I need the design to be in a standard format such that I can update the content by myself ( and does not need specialised software) as the company and business progresses.

Target Market(s)

Industry/Entity Type

Health And Wellness

Contact Information for Business Card

Card should have rounded edges. Design should have the same "feel" as the website. Contact Details of my business address, mobile phone, email and website should be included.

Coding

Coded - Design and coding required

Number of Pages Required

5+ page

Font styles to use
Script

Requirements
Must have
• Same colours as logo design. In cmyk system, the colours are: 20,60,0,0 which best result is pantone 681 and 40,40,0,0 which best result is pantone 2645. Card should include the logo design.

```html
<!DOCTYPE html>
<html lang="en">
<head>
<meta charset="utf-8">
<title>About Baby Massage – Willow Cradle Pregnancy and Baby Massage</title>
<link rel="stylesheet" href="https://fonts.googleapis.com/css2?family=Figtree:wght@400;500&family=Roboto:ital,wght@1,400&display=swap">
<style>
  :root {
    --lavender: #a09ac6;
    --orchid: #b0569c;
    --orchid-soft: #a58fc4;
    --ink: #4a4a4a;
    --body: #6a6a6a;
    --page: #f7f7f7;
    --footer: #efefef;
    --chip: #c9c9c9;
    --white: #ffffff;
  }
  * { margin: 0; padding: 0; box-sizing: border-box; }
  html, body { width: 731px; height: 1200px; overflow: hidden; }
  body {
    position: relative;
    background: var(--page);
    font-family: "Figtree", sans-serif;
    color: var(--body);
  }
  .top-bar { position: absolute; left: 0; top: 0; width: 731px; height: 51px; background: var(--lavender); }
  .menu-toggle { position: absolute; left: 620px; top: 19px; width: 19px; }
  .menu-toggle span { display: block; height: 2px; background: var(--white); margin-bottom: 3px; }
  .brand {
    position: absolute; left: 90px; top: 0; width: 167px; height: 108px;
    background: var(--white);
    clip-path: polygon(0 0, 100% 0, 100% 92%, 50% 100%, 0 92%);
    display: flex; flex-direction: column; align-items: center; justify-content: center; gap: 7px;
    text-align: center;
  }
  .brand-dot { width: 26px; height: 26px; border-radius: 50%; background: var(--orchid); }
  .brand-name { font-size: 11px; font-weight: 500; line-height: 1.3; color: var(--orchid); padding: 0 10px; }
  .page-title, .section-title {
    position: absolute; left: 90px; font-weight: 500; font-size: 19.5px; color: var(--ink);
  }
  .page-title { top: 116px; }
  .hero-photo {
    position: absolute; left: 90px; top: 153px; width: 552px; height: 273px;
    background: linear-gradient(120deg, #f6dccd 0%, #f1c3ad 45%, #f8e4d8 70%, #fbf5f1 100%);
  }
  .intro { position: absolute; left: 90px; top: 440px; width: 552px; }
  .intro p { font-size: 8.4px; line-height: 13.6px; margin-bottom: 13.6px; }
  .quote {
    position: absolute; left: 90px; top: 617px;
    font-family: "Roboto", sans-serif; font-style: italic; color: var(--orchid);
    font-size: 14.2px; line-height: 20.8px;
  }
  .quote cite {
    display: block; margin-top: 9px; font-size: 9px; color: var(--orchid-soft); font-style: italic;
  }
  .section-title { top: 758px; }
  .benefits { position: absolute; left: 90px; top: 795px; list-style: none; }
  .benefits li { font-size: 7.6px; line-height: 16.2px; color: var(--ink); }
  .benefits li::before { content: "• "; }
  .source {
    position: absolute; left: 90px; top: 1027px;
    font-family: "Roboto", sans-serif; font-style: italic; font-size: 9px; color: var(--orchid-soft);
  }
  .site-footer { position: absolute; left: 0; top: 1085px; width: 731px; height: 115px; background: var(--footer); }
  .cert-badge { position: absolute; left: 96px; top: 15px; width: 160px; height: 88px; border-radius: 6px; background: #e3dcec; }
  .footer-heading {
    position: absolute; top: 17px; font-size: 13px; font-weight: 500; color: var(--orchid);
  }
  .quick-links-title { left: 288px; }
  .follow-title { left: 534px; }
  .link-col { position: absolute; top: 37px; list-style: none; }
  .link-col li { font-size: 7.2px; line-height: 15.6px; color: var(--ink); }
  .link-col.first { left: 289px; }
  .link-col.second { left: 403px; }
  .social { position: absolute; left: 531px; top: 37px; display: flex; gap: 5px; }
  .social span { width: 20px; height: 20px; border-radius: 50%; background: var(--chip); }
  .copyright { position: absolute; left: 533px; top: 67px; font-size: 7px; color: var(--ink); }
</style>
</head>
<body>
  <header class="top-bar">
    <div class="menu-toggle" aria-label="Menu"><span></span><span></span><span></span></div>
  </header>
  <div class="brand">
    <span class="brand-dot"></span>
    <span class="brand-name">Willow Cradle<br>Pregnancy and Baby Massage</span>
  </div>

  <h1 class="page-title">About Baby Massage</h1>
  <div class="hero-photo" role="img" aria-label="Adult hands gently holding and massaging a baby's feet"></div>

  <section class="intro">
    <p>Baby massage was first described in China circa 4000 years ago, then in India and Egypt, and was passed down from mother to daughter over the generations. It has become more popular in the Western world over the last 20 to 30 years.</p>
    <p>Massage can start from birth and is a wonderful way to soothe, calm and enjoy time with your baby, as well as helping with the bonding process.</p>
    <p>Long before babies are able to talk, they communicate with the new world around them through touch. Skin sensitivity is one of the earliest functions of the body. In fact, stimulation of the skin is essential for adequate organic and psychological development.</p>
    <p>Whilst it is possible to learn the principles of baby massage from books, DVD's, and social media, there is really no substitute for learning from an experienced and qualified instructor. During classes, you will be guided through the basic strokes of Baby massage in a clear and relaxing manner. You will also learn to recognise and understand your baby's cues, which is a very important part of baby massage.</p>
  </section>

  <blockquote class="quote">
    “Being touched and caressed,<br>being massaged,<br>is food for the infant.<br>Food as necessary<br>as minerals, vitamins, and proteins.”
    <cite>(Dr Henri Valcourt -&nbsp; Renowned Obstetrician and Author.)</cite>
  </blockquote>

  <h2 class="section-title">Benefits of Baby massage</h2>
  <ul class="benefits">
    <li>Relaxation of skeletal muscles</li>
    <li>Strengthens the immune system</li>
    <li>Reduces stress hormone levels in children and parents</li>
    <li>Improves sleep and regulates sleep patterns</li>
    <li>Relieves discomfort of wind, constipation, colic and reflux; sinus and chest congestion</li>
    <li>Reduces crying</li>
    <li>Enhances attachment and bonding</li>
    <li>Reduces symptoms of eczema</li>
    <li>Enhances emotions and improves mood</li>
    <li>Improves digestive, respiratory and circulatory system</li>
    <li>Reduces postnatal depression</li>
    <li>Reduces anxiety</li>
    <li>Increases blood and lymphatic circulation</li>
    <li>Enhances cognitive and motor development</li>
  </ul>
  <p class="source">Source: ITLN (Infant Touch Learning Network)</p>

  <footer class="site-footer">
    <div class="cert-badge" role="img" aria-label="Certification badge"></div>
    <h3 class="footer-heading quick-links-title">Quick Links</h3>
    <ul class="link-col first">
      <li>Home</li><li>About Me</li><li>Benefits of Pregnancy</li><li>Benefits of Baby Massage</li>
    </ul>
    <ul class="link-col second">
      <li>Pregnancey Massage Sessions</li><li>Baby Massage Sessions</li><li>Contact</li>
    </ul>
    <h3 class="footer-heading follow-title">Follow Us</h3>
    <div class="social" aria-label="Social links"><span></span><span></span><span></span><span></span></div>
    <p class="copyright">© 2017 Willow Cradle Pregnancy</p>
  </footer>
</body>
</html>
```